Home Page for a Swiss based start up company, trading Natural & Health food ingredients (B2B)

I would like to create a home page for my new start up company (Velbrook Trade AG), the main field of activity is the trading and marketing of Natural and Health food ingredients towards the functional Food and Food supplements industry. (B2B).
Target Market : Functional Food and Food Supplement Manufacturers (B2B) based in Switzerland and Europe
The values I would like to convey are :
- sourcing of natural and health ingredients, (example : natural plant extracts, Omega 3, plant proteins, natural vitamins, vegan food ingredients...etc)
- Health & Nutritional Health
- Eco-friendly and Sustainability
- High Quality Standard in term of products and logistic services
- Trust and reliability
- Flexibility & speed to market
-Technical advice for the development of new products

The site will be translated in 3 languages (German, French, English)
Number of web pages : 5 : Home, About us, Products, Our Services, Contact

See here below attached Logo file.

Here some link of websites which can be taken as benchmark or source of inspiration
- https://quorvindel.com
- https://www.brimtaless.com/

Target Market(s)

Manufacturers of Functional Foods and Food Supplements in Switzerland and Europe (B2B)

Industry/Entity Type

B2B Trading of Natural & Health Ingredients

Font styles to use
Sans Serif

Colors
0054AA
0677BA
7BADD7
CADEEF
E8F1F8
0094D4
00A9DD
6FCCEA
C7EBF8
E9F6FB
00AB8E
00BBA5
67D7C9
C6EFE9
E9F9F6
59FF00
82FF00
B8FF75
E3FFCB
F4FFEA
FFF300
FFF600
FEFA6F
FFFEC7
FFFEE8
FFC000
F8CF3A
FAE287
FDF2CF
FEFAEE
F0912C
F2A743
F7CA91
FBE8D2
FDF5EE
EE7325
F08F49
F5BC92
FAE3D3
FDF4ED

Requirements
Must have
• inspiration towards nature, sustainability, vegan food, functional food & beverages, food supplements, nutritional health, low carbon footprint
Should not have
• animals, chemistry, food additives

```html
<!DOCTYPE html>
<html lang="en">
<head>
<meta charset="utf-8">
<title>Velbrook Trade AG – Natural &amp; Health Food Ingredients</title>
<link href="https://fonts.googleapis.com/css2?family=Poppins:wght@400;500;600;700&family=Roboto:wght@400;500;700&family=Roboto+Condensed:wght@400&family=Fira+Sans:wght@500;600&display=swap" rel="stylesheet">
<style>
:root{
  --green:#21a07c;
  --green-dark:#17906d;
  --orange:#ee6a25;
  --ink:#222;
  --muted:#666;
  --cream:#fdf4ed;
  --white:#fff;
  --faint:#ececec;
}
*{box-sizing:border-box;margin:0;padding:0}
html,body{width:1200px;height:3545px;overflow:hidden}
body{position:relative;font-family:'Roboto',sans-serif;color:var(--ink);background:var(--white)}
.abs{position:absolute}
a{color:inherit;text-decoration:none}

/* top bar */
.topbar{left:0;top:0;width:1200px;height:44px;background:var(--green);color:#fff;font:400 15px 'Poppins',sans-serif}
.topbar .phone{left:100px;top:11px;display:flex;gap:10px;align-items:center}
.topbar .mail{left:918px;top:11px;display:flex;gap:10px;align-items:center}
.topbar .socials{left:522px;top:11px;display:flex;gap:14px}
.dot{width:18px;height:18px;border-radius:50%;background:#fff;opacity:.9}
.dot.accent{background:var(--orange)}

/* hero */
.hero{left:0;top:44px;width:1200px;height:679px;background:
  radial-gradient(ellipse at 50% 100%, #5c6b2a 0%, transparent 45%),
  linear-gradient(180deg,#2a2a2a 0%,#232323 45%,#3a3520 75%,#6b4f1c 100%)}
.hero-food{left:0;top:420px;width:1200px;height:303px;background:
  linear-gradient(90deg,#c79a1e 0%,#d9541c 18%,#4f7d2a 32%,#e0b022 44%,#5a2846 58%,#6f8a2f 68%,#e9a13a 82%,#c6561d 100%);opacity:.85}
.logo{left:99px;top:66px;font:600 33px 'Poppins',sans-serif;color:#fff}
.nav{left:399px;top:77px;display:flex;gap:55px;font:500 16px 'Poppins',sans-serif;color:#fff}
.lang{left:1010px;top:68px;width:91px;height:36px;border-radius:18px;background:#5ec9b1;color:#fff;font:500 16px 'Poppins',sans-serif;display:flex;align-items:center;padding-left:14px;gap:6px}
.flag{width:26px;height:26px;border-radius:50%;overflow:hidden;display:flex;flex-direction:column}
.flag i{flex:1}
.welcome-frame{left:193px;top:179px;width:814px;height:151px;border:2px solid var(--orange);border-bottom:none}
.welcome-title{left:0;top:205px;width:1200px;text-align:center;font:400 50px 'Poppins',sans-serif;color:#fff;letter-spacing:-.5px}
.welcome-title b{color:var(--orange);font-weight:700}
.welcome-sub{left:0;top:278px;width:1200px;text-align:center;font:400 23px 'Poppins',sans-serif;color:#fff}
.btn-start{left:523px;top:328px;width:154px;height:50px;border-radius:25px;background:var(--orange);color:#fff;font:500 17px 'Poppins',sans-serif;display:flex;align-items:center;justify-content:center}

/* section titles */
.ghost{left:0;width:1200px;text-align:center;font:700 82px 'Poppins',sans-serif;color:var(--faint);letter-spacing:4px}
.sec-title{left:0;width:1200px;text-align:center;font:600 31px 'Fira Sans',sans-serif;color:var(--green);letter-spacing:1px}

/* about */
.about-ghost{top:790px}
.about-title{top:822px;font:400 34px 'Poppins',sans-serif}
.about-text{left:152px;top:896px;width:896px;text-align:center;font:400 16px/26px 'Roboto',sans-serif;color:#333}
.btn-green{background:var(--green);color:#fff;display:flex;align-items:center;justify-content:center;border-radius:26px}
.btn-read{left:526px;top:1022px;width:148px;height:52px;font:600 14px 'Poppins',sans-serif}
.leaf-deco{border-radius:50%;background:radial-gradient(circle,#eef3ea 0%,#f7f9f5 60%,transparent 70%)}

/* service */
.service-bg{left:0;top:1140px}
.service-ghost{top:1208px;color:rgba(255,255,255,.12)}
.service-title{top:1238px;color:#fff}
.card{background:#fff;border-radius:14px;overflow:hidden}
.svc{top:1344px;width:323px;height:373px}
.svc .pic{height:210px}
.svc h3{margin-top:22px;text-align:center;font:600 25px 'Fira Sans',sans-serif;color:var(--green);letter-spacing:1.5px}
.svc p{margin:14px auto 0;width:290px;text-align:center;font:400 15px/26px 'Roboto',sans-serif;color:#777}
.arrow-dark{width:44px;height:44px;border-radius:50%;background:#111;display:flex;align-items:center;justify-content:center}

/* values */
.values-ghost{top:1920px}
.values-title{top:1950px}
.value{top:2050px;width:234px;height:255px;border:2px solid #e4e4e4;border-radius:4px;background:#fff;text-align:center}
.value.active{top:2036px;border-color:#c7ece1;box-shadow:0 4px 14px rgba(0,0,0,.08)}
.value svg{margin-top:30px}
.value h4{margin-top:12px;font:500 17px/23px 'Poppins',sans-serif;color:#222;padding:0 12px}
.value.active h4{color:var(--green)}
.value p{margin-top:14px;font:400 14px/23px 'Roboto Condensed',sans-serif;color:#666;padding:0 22px}
.arrow-light{width:44px;height:44px;border-radius:50%;background:#f2f2f2;box-shadow:0 2px 6px rgba(0,0,0,.15);display:flex;align-items:center;justify-content:center}

/* blog */
.blog-bg{left:0;top:2383px;width:1200px;height:729px;background:var(--cream)}
.blog-ghost{top:2412px;color:#ede5df}
.blog-title{top:2444px}
.post{background:#fff;border:1px solid #e3e3e3}
.post-main{left:117px;top:2539px;width:513px;height:513px}
.post-main .frame{position:absolute;left:11px;top:13px;width:492px;height:246px;border:2px solid #3d3f8f;padding:9px}
.post-main .frame .pic{width:100%;height:100%}
.post-main h3{position:absolute;left:6px;top:275px;font:500 23px 'Roboto',sans-serif;color:#111}
.date{display:flex;align-items:center;gap:10px;font:400 19px 'Roboto',sans-serif;color:#444}
.post-main .date{position:absolute;left:8px;top:313px}
.post-main p{position:absolute;left:12px;top:362px;width:340px;font:400 14px/26px 'Roboto',sans-serif;color:#555}
.btn-post{width:134px;height:48px;font:400 19px 'Roboto',sans-serif}
.post-main .btn-post{position:absolute;left:15px;top:451px}
.post-side{left:654px;width:433px;height:244px}
.post-side .pic{position:absolute;left:9px;top:16px;width:181px;height:209px}
.post-side h3{position:absolute;left:206px;top:24px;font:500 20px 'Roboto',sans-serif;color:#111}
.post-side p{position:absolute;left:212px;top:60px;width:210px;font:400 14px/21px 'Roboto',sans-serif;color:#555}
.post-side .date{position:absolute;left:206px;top:114px}
.post-side .btn-post{position:absolute;left:207px;top:169px;width:156px;height:52px}

/* footer */
.footer{left:0;top:3112px;width:1200px;height:433px;background:var(--green);color:#fff}
.f-logo{left:110px;top:3175px;font:500 34px 'Poppins',sans-serif;color:#fff}
.f-about{left:112px;top:3236px;width:280px;font:400 15px/19px 'Roboto',sans-serif;color:#fff}
.f-social{left:106px;top:3312px;display:flex;gap:22px;align-items:center}
.f-social .dot{width:14px;height:14px}
.f-social .big{width:36px;height:36px;border-radius:50%;background:var(--orange)}
.f-head{top:3175px;font:600 19px 'Poppins',sans-serif;color:#fff;letter-spacing:.5px}
.f-list{top:3231px;list-style:none;font:400 15px 'Roboto',sans-serif}
.f-list li{height:28px;display:flex;align-items:center;gap:8px}
.f-list li::before{content:"»";font-size:14px}
.f-contact{left:841px;display:flex;gap:18px;align-items:center;font:400 15px/24px 'Roboto',sans-serif;color:#fff}
.f-rule{left:110px;top:3436px;width:980px;height:1px;background:rgba(255,255,255,.25)}
.copy{left:0;top:3474px;width:1200px;text-align:center;font:400 14px 'Roboto',sans-serif;color:#fff}
</style>
</head>
<body>

<!-- top bar -->
<div class="abs topbar">
  <div class="abs phone">
    <svg width="20" height="20" viewBox="0 0 24 24" fill="none" stroke="#fff" stroke-width="1.5"><circle cx="12" cy="12" r="10.5"/><path d="M8.5 7.5l2 2-1 1.5c.8 1.6 1.9 2.7 3.5 3.5l1.5-1 2 2-1.2 1.5c-3.8-.6-7.2-4-7.8-7.8z"/></svg>
    <span>+1 88 888 8888</span>
  </div>
  <div class="abs socials"><span class="dot"></span><span class="dot"></span><span class="dot"></span><span class="dot accent"></span><span class="dot"></span></div>
  <div class="abs mail">
    <svg width="24" height="18" viewBox="0 0 24 18" fill="none" stroke="#fff" stroke-width="1.5"><rect x="1" y="1" width="22" height="16" rx="1"/><path d="M1 1l11 9 11-9"/></svg>
    <span>info@velbrooktrade.com</span>
  </div>
</div>

<!-- hero -->
<header class="abs hero" role="img" aria-label="Dark slate table with fresh vegetables, spices and herbs along the bottom edge"></header>
<div class="abs hero-food" role="img" aria-label="Peppers, citrus, avocado, onions, carrots and bowls of spices"></div>
<div class="abs logo">Velbrook Trade</div>
<nav class="abs nav"><a>HOME</a><a>ABOUT</a><a>SERVICES</a><a>OUR VALAUE</a><a>CONTACT</a></nav>
<div class="abs lang">EN- <span class="flag"><i style="background:#111"></i><i style="background:#dd1f1f"></i><i style="background:#f5c400"></i></span></div>
<div class="abs welcome-frame"></div>
<h1 class="abs welcome-title">WELCOME TO <b>Velbrook Trade</b></h1>
<p class="abs welcome-sub">Trading Natural &amp; Health food ingredients</p>
<a class="abs btn-start">Get Started</a>

<!-- about -->
<div class="abs leaf-deco" style="left:1030px;top:760px;width:200px;height:200px" role="img" aria-label="Faint bowl of greens decoration"></div>
<div class="abs leaf-deco" style="left:-40px;top:1000px;width:220px;height:200px" role="img" aria-label="Faint bowl of greens decoration"></div>
<div class="abs ghost about-ghost">WHAT WE &nbsp;DO</div>
<h2 class="abs sec-title about-title">ABOUT US</h2>
<p class="abs about-text">Lorem ipsum dolor sit amet, consectetur adipiscing elit, sed do eiusmod tempor incididunt ut labore et dolore magna aliqua. Ut enim ad minim veniam, quis nostrud exercitation ullamco laboris nisi ut aliquip ex ea commodo consequat. Duis aute irure dolor in reprehenderit in voluptate velit esse cillum dolore eu fugiat nulla pariatur. Excepteur sint occaecat cupidatat non proident, sunt in culpa qui officia deserunt mollit anim id est laborum."</p>
<a class="abs btn-green btn-read">READ MORE</a>

<!-- service -->
<svg class="abs service-bg" width="1200" height="720" viewBox="0 0 1200 720">
  <path d="M420 18 C700 -10 1000 0 1200 38 L1200 60 C1000 20 700 15 420 30 Z" fill="#ee6a25"/>
  <path d="M0 88 C300 30 700 0 1000 16 C1100 22 1160 34 1200 44 L1200 632 C1000 690 700 712 400 712 C200 712 80 700 0 690 Z" fill="#21a07c"/>
  <path d="M0 685 C150 705 350 715 560 712 C360 722 160 718 0 708 Z" fill="#ee6a25"/>
</svg>
<div class="abs ghost service-ghost">FOUCE AREA</div>
<h2 class="abs sec-title service-title">OUR SERVICE</h2>

<article class="abs card svc" style="left:99px">
  <div class="pic" role="img" aria-label="Rows of bowls filled with colourful spices and seeds" style="background:linear-gradient(135deg,#7a3b2a,#b8862a 40%,#5d6b2c 70%,#8a2a2a)"></div>
  <h3>NATURE</h3>
  <p>Lorem ipsum dolor sit amet, consectetur adipiscing elit, sed do eiusmod tempor incididunt ut labore et dolore magna</p>
</article>
<article class="abs card svc" style="left:438px">
  <div class="pic" role="img" aria-label="Farmer tending leafy crops in a field" style="background:linear-gradient(180deg,#c9d6df 0%,#8fa27a 45%,#3f5a2e 100%)"></div>
  <h3>SUSTAINABILITY</h3>
  <p>Lorem ipsum dolor sit amet, consectetur adipiscing elit, sed do eiusmod tempor incididunt ut labore et dolore magna</p>
</article>
<article class="abs card svc" style="left:776px">
  <div class="pic" role="img" aria-label="Fresh green vegetables and pears on a light table" style="background:linear-gradient(135deg,#e9ecdf,#7fae3e 45%,#3f6b22 75%,#d7d2b8)"></div>
  <h3>VEGAN FOOD</h3>
  <p>Lorem ipsum dolor sit amet, consectetur adipiscing elit, sed do eiusmod tempor incididunt ut labore et dolore magna</p>
</article>
<div class="abs arrow-dark" style="left:25px;top:1525px"><svg width="14" height="14" viewBox="0 0 14 14" fill="none" stroke="#fff" stroke-width="1.6"><path d="M9 2L4 7l5 5"/></svg></div>
<div class="abs arrow-dark" style="left:1132px;top:1525px"><svg width="14" height="14" viewBox="0 0 14 14" fill="none" stroke="#fff" stroke-width="1.6"><path d="M5 2l5 5-5 5"/></svg></div>

<!-- values -->
<div class="abs ghost values-ghost">BENEFITS</div>
<h2 class="abs sec-title values-title">OUR VALUES</h2>

<div class="abs value" style="left:113px">
  <svg width="90" height="90" viewBox="0 0 90 90" fill="none" stroke="#111" stroke-width="2.5" stroke-linejoin="round">
    <path d="M45 50 C30 38 22 30 22 20 a11 11 0 0 1 23-3 a11 11 0 0 1 23 3 c0 10-8 18-23 30z"/>
    <path d="M45 22v14M38 29h14"/>
    <path d="M8 40l6 22 14 14h10V62L26 50M82 40l-6 22-14 14H52V62l12-12"/>
  </svg>
  <h4>Health &amp; Nutritional Health</h4>
  <p>We do a free evaluation to be sure you want to start selling.</p>
</div>
<div class="abs value active" style="left:360px">
  <svg width="90" height="90" viewBox="0 0 90 90" fill="none" stroke="#21a07c" stroke-width="2.5" stroke-linecap="round">
    <path d="M20 30 A30 30 0 0 1 70 26M70 60 A30 30 0 0 1 20 64"/>
    <path d="M64 18l6 8-9 3M26 72l-6-8 9-3"/>
    <path d="M34 58 C34 40 46 32 58 32 C58 46 50 58 34 58z M34 58 L50 42"/>
  </svg>
  <h4>Eco-friendly and Sustainability</h4>
  <p>We do a free evaluation to be sure you want to start selling.</p>
</div>
<div class="abs value" style="left:607px">
  <svg width="90" height="90" viewBox="0 0 90 90" fill="none" stroke="#111" stroke-width="2.5" stroke-linejoin="round">
    <path d="M45 6l7 5 9-1 3 8 8 4-1 9 5 7-5 7 1 9-8 4-3 8-9-1-7 5-7-5-9 1-3-8-8-4 1-9-5-7 5-7-1-9 8-4 3-8 9 1z"/>
    <circle cx="45" cy="39" r="16"/><path d="M37 39l6 6 10-11"/>
    <path d="M30 64l-6 20 9-4 5 8 6-16M60 64l6 20-9-4-5 8-6-16"/>
  </svg>
  <h4>High Quality Standard in term of products</h4>
  <p>We do a free evaluation to be sure you want to start selling.</p>
</div>
<div class="abs value" style="left:854px">
  <svg width="90" height="90" viewBox="0 0 90 90" fill="none" stroke="#111" stroke-width="2.5" stroke-linejoin="round">
    <path d="M45 86V40 M45 40l-8-10v-8h-6l14-16 14 16h-6v8z"/>
    <path d="M45 60 L22 42 h-8 v6 l-10-12 10-12 v6 h10 l15 12"/>
    <path d="M52 48 L68 36 h6 v-6 l12 12-12 12 v-6 h-6 l-16 14"/>
  </svg>
  <h4>Flexibility &amp; speed to market</h4>
  <p>We do a free evaluation to be sure you want to start selling.</p>
</div>
<div class="abs arrow-light" style="left:47px;top:2163px"><svg width="12" height="12" viewBox="0 0 14 14" fill="none" stroke="#21a07c" stroke-width="1.8"><path d="M9 2L4 7l5 5"/></svg></div>
<div class="abs arrow-light" style="left:1104px;top:2163px"><svg width="12" height="12" viewBox="0 0 14 14" fill="none" stroke="#21a07c" stroke-width="1.8"><path d="M5 2l5 5-5 5"/></svg></div>

<!-- blog -->
<div class="abs blog-bg"></div>
<div class="abs ghost blog-ghost">NEWS</div>
<h2 class="abs sec-title blog-title">OUR BLOG</h2>

<article class="abs post post-main">
  <div class="frame"><div class="pic" role="img" aria-label="Woman in a bright kitchen holding a green apple" style="background:linear-gradient(90deg,#c8cbcc 0%,#e0d8d0 40%,#d2588f 55%,#e7e3df 75%,#cfd1d2 100%)"></div></div>
  <h3>Lorem ipsum dolor sit amet, consectetur</h3>
  <div class="date"><svg width="18" height="18" viewBox="0 0 18 18" fill="none" stroke="#555" stroke-width="1.4"><rect x="1" y="3" width="16" height="14"/><path d="M1 7h16M5 1v4M13 1v4M5 10h2M9 10h2M13 10h1M5 13h2M9 13h2"/></svg>27April, 2022</div>
  <p>Lorem ipsum dolor sit amet, consectetur adipiscing elit, sed do eiusmod tempor incididunt ut labore et dolore magna aliqua.</p>
  <a class="btn-green btn-post">Read more</a>
</article>

<article class="abs post post-side" style="top:2539px">
  <div class="pic" role="img" aria-label="Bowl of fresh salad on a dark surface" style="background:radial-gradient(circle at 55% 40%,#6a9a34 0%,#b8402a 25%,#2a2a2a 55%,#1d1d1d 100%)"></div>
  <h3>Lorem ipsum dolor sit</h3>
  <p>Lorem ipsum dolor sit amet, consectetur adipiscing elit, sed</p>
  <div class="date"><svg width="18" height="18" viewBox="0 0 18 18" fill="none" stroke="#555" stroke-width="1.4"><rect x="1" y="3" width="16" height="14"/><path d="M1 7h16M5 1v4M13 1v4M5 10h2M9 10h2M13 10h1M5 13h2M9 13h2"/></svg>27April, 2022</div>
  <a class="btn-green btn-post">Read more</a>
</article>
<article class="abs post post-side" style="top:2808px">
  <div class="pic" role="img" aria-label="Assortment of fruit, vegetables, grains and bread" style="background:linear-gradient(135deg,#6b8a3a 0%,#d86a3a 35%,#a0663a 55%,#e5b83a 75%,#6a3a5a 100%)"></div>
  <h3>Lorem ipsum dolor sit</h3>
  <p>Lorem ipsum dolor sit amet, consectetur adipiscing elit, sed</p>
  <div class="date"><svg width="18" height="18" viewBox="0 0 18 18" fill="none" stroke="#555" stroke-width="1.4"><rect x="1" y="3" width="16" height="14"/><path d="M1 7h16M5 1v4M13 1v4M5 10h2M9 10h2M13 10h1M5 13h2M9 13h2"/></svg>27April, 2022</div>
  <a class="btn-green btn-post">Read more</a>
</article>

<!-- footer -->
<footer class="abs footer"></footer>
<div class="abs f-logo">Velbrook Trade</div>
<p class="abs f-about">Lorem ipsum dolor sit amet, consectetur adipiscing elit, sed do eiusmod tempor incididunt ut labore et dolore magna</p>
<div class="abs f-social"><span class="big"></span><span class="dot"></span><span class="dot"></span><span class="dot"></span></div>

<h4 class="abs f-head" style="left:425px">MENU</h4>
<ul class="abs f-list" style="left:427px"><li>Home</li><li>About</li><li>Services</li><li>Our valaue</li><li>Contact</li></ul>
<h4 class="abs f-head" style="left:617px">HELP LINK</h4>
<ul class="abs f-list" style="left:619px"><li>Terms&amp;condtions</li><li>Privacy Policy</li><li>About Us</li><li>Support</li></ul>
<h4 class="abs f-head" style="left:841px">OUR LOCATION</h4>

<div class="abs f-contact" style="top:3220px">
  <svg width="34" height="34" viewBox="0 0 34 34" fill="none" stroke="#fff" stroke-width="1.5"><circle cx="17" cy="17" r="16"/><path d="M17 26s-6-6.5-6-11a6 6 0 0 1 12 0c0 4.5-6 11-6 11z"/><circle cx="17" cy="15" r="2"/></svg>
  <span>1472 Lorem ipsum dolor sit<br>amet, consectetur</span>
</div>
<div class="abs f-contact" style="top:3301px">
  <svg width="34" height="34" viewBox="0 0 34 34" fill="none" stroke="#fff" stroke-width="1.5"><circle cx="17" cy="17" r="16"/><path d="M12 10l3 3-1.5 2c1 2 2.5 3.5 4.5 4.5l2-1.5 3 3-2 2c-5-1-9-5-10-10z"/></svg>
  <span>+1 888 888 8888</span>
</div>
<div class="abs f-contact" style="top:3366px">
  <svg width="34" height="34" viewBox="0 0 34 34" fill="none" stroke="#fff" stroke-width="1.5"><circle cx="17" cy="17" r="16"/><rect x="10" y="12" width="14" height="10" rx="1"/><path d="M10 12l7 6 7-6"/></svg>
  <span>hello@velbrooktrade.com</span>
</div>
<div class="abs f-rule"></div>
<p class="abs copy">© copyrights 2022 &nbsp;velbrooktrade | &nbsp;All Rights Reserved</p>

</body>
</html>
```